Packaging Design job - Health Supplement

We need a packaging design theme for a health supplement for Moroccan consumers. Our product is called 'Velmarine'. https://corvelsante.example/nos-produits/digestion/vel-marine/

It is a unique solution of three plants with recognized benefits. The activated carbon in the product allows, like plants, reduce effectively the problems related to digestion. The product is particularly effective for soothing bloating and optimizing intestinal transit as well as digestion.

We would like to see clean, modern and fresh designs.
This should give the impression of professional products of pharmaceutical quality.

You will find attached the current packaging design of the product. what we do not like:
- The design is not modern
- The design does not evoke the purpose of the product

You will also find attached the logo of our company.

Ps : You can change the color of the logo

Font styles to use
Serif
Sans Serif

Colors

Designer to choose colors to be used in the design.

Requirements
Must have
• - Bottle and box packaging required.
• - Product is bottle of 30 tablets
Should not have
• Sales and other "must buy" "guaranteed" etc

```html
<!DOCTYPE html>
<html lang="fr">
<head>
<meta charset="utf-8">
<title>Vel-Marine – Packaging</title>
<link rel="stylesheet" href="https://fonts.googleapis.com/css2?family=Oswald:wght@400;500;600&family=Open+Sans:wght@400;600;700&display=swap">
<style>
  :root {
    --bg: #eceeed;
    --plum: #7a5685;
    --plum-dark: #6c4a77;
    --wine: #9b2d45;
    --wine-dark: #86263b;
    --kraft: #c4b3a1;
    --neck: #f4f4f2;
  }
  * { box-sizing: border-box; margin: 0; padding: 0; }
  html, body { width: 1200px; height: 689px; overflow: hidden; }
  body { background: var(--bg); position: relative; font-family: "Open Sans", sans-serif; }

  .bottle { position: absolute; top: 190px; width: 232px; height: 395px; }
  .bottle--plum { left: 222px; --tone: var(--plum); --tone-dark: var(--plum-dark); }
  .bottle--wine { left: 478px; --tone: var(--wine); --tone-dark: var(--wine-dark); }
  .bottle__cap { position: absolute; left: 23px; top: 0; width: 186px; height: 60px; background: var(--tone-dark); border-radius: 14px 14px 6px 6px; }
  .bottle__neck { position: absolute; left: 30px; top: 58px; width: 172px; height: 22px; background: var(--neck); }
  .bottle__body { position: absolute; left: 0; top: 78px; width: 232px; height: 317px; background: var(--tone); border-radius: 36px 36px 18px 18px; }
  .bottle__label { position: absolute; left: 0; top: 60px; width: 232px; height: 195px; background: var(--kraft); color: var(--tone); padding: 20px 14px 0 14px; }

  .brand { display: flex; align-items: center; gap: 5px; }
  .brand__mark { width: 9px; height: 9px; border-radius: 50%; background: currentColor; }
  .brand__name { font-family: "Open Sans", sans-serif; font-weight: 700; font-size: 11px; letter-spacing: .3px; text-transform: uppercase; }
  .brand__tag { font-size: 3.5px; margin: 2px 0 0 14px; text-transform: uppercase; opacity: .85; }

  .count { position: absolute; right: 14px; top: 12px; text-align: center; font-family: "Open Sans", sans-serif; }
  .count__num { display: block; font-weight: 700; font-size: 16px; line-height: 1; }
  .count__unit { display: block; font-weight: 600; font-size: 6px; }

  .product { font-family: "Oswald", sans-serif; font-weight: 600; font-size: 29px; line-height: 1; margin-top: 58px; }
  .plants { font-family: "Oswald", sans-serif; font-weight: 500; font-size: 12.5px; line-height: 1.4; margin-top: 4px; }

  .box { position: absolute; left: 730px; top: 140px; width: 286px; height: 418px; background: var(--kraft); color: var(--wine); }
  .box__band { position: absolute; left: 0; width: 100%; background: var(--wine); }
  .box__band--top { top: 0; height: 96px; }
  .box__band--bottom { bottom: 0; height: 74px; }
  .box__brand { position: absolute; left: 18px; top: 124px; }
  .box .brand__name { font-size: 13px; }
  .box .count { right: 22px; top: 108px; }
  .box .count__num { font-size: 22px; }
  .box .count__unit { font-size: 9px; }
  .box__product { position: absolute; left: 26px; top: 224px; font-family: "Open Sans", sans-serif; font-weight: 400; font-size: 27px; letter-spacing: .4px; line-height: 1.2; }
  .box__plants { position: absolute; left: 30px; top: 262px; font-size: 6.5px; color: var(--wine); letter-spacing: .3px; }
  .benefits { position: absolute; left: 26px; top: 276px; list-style: none; color: var(--wine); font-size: 12.5px; line-height: 1.45; letter-spacing: .6px; word-spacing: 2px; }
  .benefits li::before { content: "\2022"; font-size: 8px; margin-right: 3px; vertical-align: middle; }
</style>
</head>
<body>
  <div class="bottle bottle--plum">
    <div class="bottle__cap"></div>
    <div class="bottle__neck"></div>
    <div class="bottle__body">
      <div class="bottle__label">
        <div class="brand"><span class="brand__mark"></span><span class="brand__name">Orvanelle</span></div>
        <p class="brand__tag">Soins naturels et équilibre digestif</p>
        <div class="count"><span class="count__num">30</span><span class="count__unit">Capsules</span></div>
        <h2 class="product">VEL-MARINE</h2>
        <p class="plants">FENNEL-ANIS VERT-CARVI NOIR<br>FENOUIL-GREEN ANISE-BLACK CARAWAY</p>
      </div>
    </div>
  </div>

  <div class="bottle bottle--wine">
    <div class="bottle__cap"></div>
    <div class="bottle__neck"></div>
    <div class="bottle__body">
      <div class="bottle__label">
        <div class="brand"><span class="brand__mark"></span><span class="brand__name">Orvanelle</span></div>
        <p class="brand__tag">Soins naturels et équilibre digestif</p>
        <div class="count"><span class="count__num">30</span><span class="count__unit">Capsules</span></div>
        <h2 class="product">VEL-MARINE</h2>
        <p class="plants">FENNEL-ANIS VERT-CARVI NOIR<br>FENOUIL-GREEN ANISE-BLACK CARAWAY</p>
      </div>
    </div>
  </div>

  <div class="box">
    <div class="box__band box__band--top"></div>
    <div class="box__brand">
      <div class="brand"><span class="brand__mark"></span><span class="brand__name">Orvanelle</span></div>
      <p class="brand__tag">Soins naturels et équilibre digestif</p>
    </div>
    <div class="count"><span class="count__num">30</span><span class="count__unit">Gelules</span></div>
    <h1 class="box__product">VEL-MARINE</h1>
    <p class="box__plants">Fennel, Green Anise, Black Caraway, Fenouil, Anis vert, Carvi noir</p>
    <ul class="benefits">
      <li>Facilite le transit</li>
      <li>Ameliore la digestion</li>
      <li>Effet ventre plat</li>
    </ul>
    <div class="box__band box__band--bottom"></div>
  </div>
</body>
</html>
```